Banner Ad Design Project

I need banners made for the following site: http://www.velmorquistanbo.com

Sizes needed are:

728x90
200x200
160x600
120x600
300x250
336x280

Info:

You do not have to theme it around the colors used on the website. You can create your own colors if you want.

Taglines that you can use are:

"Learn how to receive hundreds of messages from women in less than an hour using a new software tool"

"Hack online dating websites and bombard your inbox with eager women wanting to learn more about you"

"Boost your dating site profile views by 486%"

"BANNED! Find out why this software tool that messages hundreds of women in minutes was banned by the online dating websites. Click Here"

I am looking for good calls to action, spark curiosity, and a clickable ad. Please ask any and all questions.

Target Market(s)

Single Men 18-45

Industry/Entity Type

Software

Requirements
Must have
• - Call to action (i.e. Click Here, Download Now, etc)
- Clear easy to read font, colors, and design.
- Must be 50kb or smaller to use on bidplume. If you have design that is over submit draft and I might make exception.

```html
<!DOCTYPE html>
<html lang="en">
<head>
<meta charset="utf-8">
<title>Velmor Quistanbo – Banner Set</title>
<link rel="stylesheet" href="https://fonts.googleapis.com/css2?family=Oswald:wght@500;600&family=Open+Sans:wght@400;600&display=swap">
<style>
  :root {
    --page: #ece8e4;
    --red-bright: #e8282c;
    --red-mid: #a8151a;
    --red-deep: #5c0709;
    --red-night: #2a0304;
    --maroon: #4a0508;
    --salmon: #f39a86;
    --blush: #f6d6cf;
    --ink-white: #ffffff;
    --button-top: #f0464a;
    --button-bottom: #b81419;
    --rule: rgba(255,255,255,0.25);
  }
  * { box-sizing: border-box; margin: 0; padding: 0; }
  html, body { width: 1200px; height: 900px; overflow: hidden; }
  body { background: var(--page); position: relative; font-family: "Open Sans", sans-serif; color: var(--ink-white); }

  .banner {
    position: absolute; overflow: hidden;
    background: linear-gradient(180deg, var(--red-bright) 0%, var(--red-mid) 45%, var(--red-deep) 100%);
    box-shadow: 0 3px 8px rgba(0,0,0,0.25);
  }

  /* Area reserved for the dancing-crowd artwork: soft gradient in its tones */
  .crowd {
    position: absolute;
    background:
      linear-gradient(180deg, rgba(232,40,44,0) 70%, rgba(200,30,34,0.9) 100%),
      linear-gradient(90deg,
        var(--maroon) 0%, #8e1015 14%, var(--blush) 26%, #a3161b 36%,
        var(--maroon) 48%, #b01a1f 58%, var(--maroon) 68%,
        #c8413a 80%, var(--salmon) 90%, #d2322f 100%);
  }

  .headline, .kicker, .you { font-family: "Oswald", sans-serif; font-weight: 600; line-height: 1.08; position: absolute; }
  .support { position: absolute; font-weight: 400; line-height: 1.15; }

  .cta {
    position: absolute; display: flex; align-items: center; justify-content: center;
    font-weight: 600; color: var(--ink-white);
    background: linear-gradient(180deg, var(--button-top), var(--button-bottom));
    border: 2px solid var(--ink-white); border-left: none;
    border-radius: 0 22px 22px 0;
  }
  .cta.flush-right { border-left: 2px solid var(--ink-white); border-right: none; border-radius: 22px 0 0 22px; }

  .brand { position: absolute; display: flex; align-items: center; gap: 8px; }
  .brand-dot { width: 26px; height: 26px; border-radius: 50%; background: var(--red-bright); flex: none; }
  .brand-name { font-weight: 600; color: var(--ink-white); line-height: 1.05; text-align: left; }

  .footer-band { position: absolute; left: 0; right: 0; bottom: 0; background: linear-gradient(180deg, var(--red-night), #120102); }

  /* Skyscraper */
  .skyscraper { left: 70px; top: 77px; width: 192px; height: 715px; text-align: center; }
  .skyscraper .crowd { left: 0; top: 0; width: 192px; height: 184px; }
  .skyscraper .headline { left: 0; right: 0; top: 190px; font-size: 31px; }
  .skyscraper .support { left: 0; right: 0; top: 308px; font-size: 19px; }
  .skyscraper .kicker { left: 0; right: 0; top: 398px; font-size: 23px; }
  .skyscraper .you { left: 0; right: 0; top: 478px; font-size: 60px; }
  .skyscraper .cta { left: 0; top: 570px; width: 172px; height: 44px; font-size: 19px; }
  .skyscraper .footer-band { height: 92px; }
  .skyscraper .brand { left: 22px; top: 644px; }
  .skyscraper .brand-name { font-size: 16px; }

  /* Leaderboard */
  .leaderboard { left: 275px; top: 77px; width: 867px; height: 107px; background: linear-gradient(90deg, var(--red-bright) 0%, var(--red-mid) 40%, var(--red-deep) 100%); }
  .leaderboard .crowd {
    left: 0; top: 0; width: 220px; height: 107px;
    background: linear-gradient(90deg,
      var(--maroon) 0%, #8e1015 12%, var(--blush) 24%, #a3161b 34%,
      var(--maroon) 46%, #b01a1f 58%, var(--maroon) 70%,
      var(--salmon) 84%, rgba(200,40,40,0) 100%);
  }
  .leaderboard .headline { left: 222px; width: 118px; top: 8px; font-size: 21px; text-align: center; }
  .leaderboard .rule { position: absolute; top: 14px; width: 1px; height: 80px; background: var(--rule); }
  .leaderboard .support { left: 350px; width: 124px; top: 14px; font-size: 16px; text-align: center; }
  .leaderboard .kicker { left: 486px; width: 122px; top: 17px; font-size: 23px; text-align: center; }
  .leaderboard .you { left: 612px; width: 110px; top: 8px; font-size: 50px; text-align: center; }
  .leaderboard .cta { left: 739px; top: 11px; width: 128px; height: 38px; font-size: 17px; }
  .leaderboard .brand { left: 758px; top: 62px; gap: 6px; }
  .leaderboard .brand-dot { width: 22px; height: 22px; }
  .leaderboard .brand-name { font-size: 14px; }

  /* Rectangle */
  .rectangle { left: 274px; top: 211px; width: 402px; height: 333px; text-align: center; }
  .rectangle .crowd { left: 0; top: 0; width: 402px; height: 182px; }
  .rectangle .headline { left: 0; right: 0; top: 180px; font-size: 27px; }
  .rectangle .support { left: 0; right: 0; top: 218px; font-size: 13px; }
  .rectangle .kicker { left: 0; right: 0; top: 236px; font-size: 21px; }
  .rectangle .footer-band { height: 66px; }
  .rectangle .cta { left: 0; top: 275px; width: 190px; height: 44px; font-size: 19px; }
  .rectangle .brand { left: 232px; top: 286px; }
  .rectangle .brand-name { font-size: 17px; }
</style>
</head>
<body>

  <section class="banner skyscraper" aria-label="Skyscraper banner">
    <div class="crowd" role="img" aria-label="Silhouettes of dancing women in dark red, white and salmon tones"></div>
    <h2 class="headline">Hack online<br>dating<br>websites</h2>
    <p class="support">bombard your<br>inbox with<br>eager women</p>
    <p class="kicker">wanting<br>to learn<br>more about</p>
    <p class="you">“you”</p>
    <a class="cta">Learn How</a>
    <div class="footer-band"></div>
    <div class="brand"><span class="brand-dot"></span><span class="brand-name">Velmor<br>Quistanbo</span></div>
  </section>

  <section class="banner leaderboard" aria-label="Leaderboard banner">
    <div class="crowd" role="img" aria-label="Silhouettes of dancing women in dark red, white and salmon tones"></div>
    <h2 class="headline">Hack online<br>dating<br>websites</h2>
    <span class="rule" style="left:345px"></span>
    <p class="support">bombard your<br>inbox with<br>eager women<br>wanting</p>
    <span class="rule" style="left:480px"></span>
    <p class="kicker">to learn<br>more about</p>
    <span class="rule" style="left:610px"></span>
    <p class="you">“you”</p>
    <a class="cta flush-right">Learn How</a>
    <div class="brand"><span class="brand-dot"></span><span class="brand-name">Velmor<br>Quistanbo</span></div>
  </section>

  <section class="banner rectangle" aria-label="Rectangle banner">
    <div class="crowd" role="img" aria-label="Silhouettes of dancing women in dark red, white and salmon tones"></div>
    <h2 class="headline">Hack online dating websites</h2>
    <p class="support">bombard your inbox with eager women</p>
    <p class="kicker">wanting to learn more about “you”</p>
    <div class="footer-band"></div>
    <a class="cta">Learn How</a>
    <div class="brand"><span class="brand-dot"></span><span class="brand-name">Velmor<br>Quistanbo</span></div>
  </section>

</body>
</html>
```